Business card design needed

Hello, I Need a business card for a company that specialises in providing contract management services for civil construction projects - roads, bridges etc.
I do have a logo that i produced for PLOVER Civilworks however it probably needs a little work, the circles dont have defined edges, i was thinking the colours should reflect the dry interior of Australia progressing out to the colours of the ocean as you move towards the East.... that was my thinking anyway!
Target Market(s)
Professional people generally 30+ yrs old who need professional services to deliver contracts in a high risk environment
Industry/Entity Type
Construction
Contact Information for Business Card
PLOVER Civilworks
Darren Holbeck - Director and Principal Engineer
Registered Professional Engineer of Queensland
Phone 0438 615 272
Email darren@plovercivilworks.com.au
ABN 83 214 570 618
Logo Text
PLOVER Civilworks
Logo styles of interest
Pictorial/Combination Logo
Wordmark Logo
Lettermark Logo
Look and feel

```html
<!DOCTYPE html>
<html lang="en">
<head>
<meta charset="utf-8">
<title>PLOVER Civilworks — Business Card</title>
<link rel="stylesheet" href="https://fonts.googleapis.com/css2?family=Arimo:wght@400;700&display=swap">
<style>
  :root {
    --page-bg: #e4e2df;
    --card-dark-top: #5a5a5a;
    --card-dark-bottom: #1e1e1e;
    --card-light: #f7f7f7;
    --ink: #1c1c1c;
    --ink-soft: #2e2e2e;
    --accent-blue: #1f78c8;
    --earth-brown: #6b4a22;
    --white: #ffffff;
  }
  * { margin: 0; padding: 0; box-sizing: border-box; }
  html, body {
    width: 1200px; height: 997px; overflow: hidden;
    background: var(--page-bg);
    font-family: "Arimo", Arial, sans-serif;
  }
  .canvas { position: relative; width: 1200px; height: 997px; }

  .card {
    position: absolute;
    width: 760px; height: 422px;
    border-radius: 4px;
    box-shadow: 0 10px 28px rgba(0,0,0,0.25);
    overflow: hidden;
  }

  /* Back of card */
  .card-back {
    left: 70px; top: 70px;
    background: radial-gradient(ellipse at 45% 40%, var(--card-dark-top) 0%, var(--card-dark-bottom) 85%);
  }
  .card-back .brand {
    position: absolute; left: 90px; top: 150px;
    display: flex; align-items: center; gap: 26px;
  }
  .brand-dot {
    width: 96px; height: 96px; border-radius: 50%;
    background: var(--earth-brown);
    flex: none;
  }
  .card-back .brand-name {
    color: var(--white);
    font-size: 44px; font-weight: 400; letter-spacing: 4px;
  }

  /* Front of card */
  .card-front {
    left: 360px; top: 500px;
    background: var(--card-light);
  }
  .card-front .brand {
    position: absolute; left: 40px; top: 34px;
    display: flex; align-items: center; gap: 22px;
  }
  .card-front .brand-dot { width: 74px; height: 74px; }
  .card-front .brand-name {
    color: var(--ink);
    font-size: 36px; font-weight: 400; letter-spacing: 4px;
  }
  .contact {
    position: absolute; left: 200px; top: 132px; width: 420px;
    text-align: center;
  }
  .person-name {
    color: var(--accent-blue);
    font-size: 24px; font-weight: 400; margin-bottom: 6px;
  }
  .person-role {
    color: var(--ink-soft);
    font-size: 17px; line-height: 23px; letter-spacing: 1px;
  }
  .details {
    margin-top: 22px;
    font-size: 16px; line-height: 25px; letter-spacing: 1px;
    color: var(--ink-soft);
  }
  .details .label { color: var(--accent-blue); }
  .card-front .footer-mark {
    position: absolute; left: 50%; bottom: 26px;
    transform: translateX(-50%);
    width: 58px; height: 58px; border-radius: 50%;
    background: var(--earth-brown);
  }
</style>
</head>
<body>
<main class="canvas">
  <section class="card card-back" aria-label="Card back">
    <div class="brand">
      <span class="brand-dot"></span>
      <span class="brand-name">PLOVER Civilworks</span>
    </div>
  </section>

  <section class="card card-front" aria-label="Card front">
    <div class="brand">
      <span class="brand-dot"></span>
      <span class="brand-name">PLOVER Civilworks</span>
    </div>
    <div class="contact">
      <p class="person-name">Darren Holbeck</p>
      <p class="person-role">Director and Principal Engineer</p>
      <p class="person-role">Registered Professional Engineer of Queensland</p>
      <div class="details">
        <p><span class="label">Phone :</span> 0438 615 272</p>
        <p><span class="label">Email :</span> darren@plovercivilworks.com.au</p>
        <p><span class="label">ABN</span> 83 214 570 618</p>
      </div>
    </div>
    <span class="footer-mark"></span>
  </section>
</main>
</body>
</html>
```